BrimstoneHoldingsLLC

Real Estate Investment. Buy/Sell house/investment . Trustworthy,Reliable, and friendly

Industry/Entity Type

Real Estate

Contact Information for Business Card

BrimstoneHoldings@mailtrove.com
555-413-2960
Tamsin-Leigh Okafor

```html
<!DOCTYPE html>
<html lang="en">
<head>
<meta charset="utf-8">
<title>Brimstone Holdings LLC — Business Card</title>
<link rel="stylesheet" href="https://fonts.googleapis.com/css2?family=Arimo:wght@400;700&family=Roboto:wght@300;400&display=swap">
<style>
  :root {
    --paper: #ffffff;
    --edge: #1a1a1a;
    --panel: #bcbdbf;
    --panel-text: #ffffff;
    --mark-fill: #e6e7e8;
    --name-ink: #333333;
    --contact-ink: #3a3a3a;
  }
  * { margin: 0; padding: 0; box-sizing: border-box; }
  html, body {
    width: 1200px;
    height: 698px;
    overflow: hidden;
    background: var(--paper);
  }
  .card {
    position: relative;
    width: 1200px;
    height: 698px;
    background: var(--paper);
  }
  .card-edge {
    position: absolute;
    left: 0;
    top: 0;
    width: 2px;
    height: 698px;
    background: var(--edge);
  }
  .brand-panel {
    position: absolute;
    left: 24px;
    top: 58px;
    width: 562px;
    height: 588px;
    background: var(--panel);
  }
  .brand-square {
    position: absolute;
    left: 186px;
    top: 78px;
    width: 190px;
    height: 190px;
  }
  .brand-name {
    position: absolute;
    left: 0;
    right: 0;
    top: 300px;
    text-align: center;
    font-family: "Roboto", "Helvetica Neue", Arial, sans-serif;
    font-size: 38px;
    font-weight: 400;
    color: var(--panel-text);
    letter-spacing: 0.5px;
  }
  .brand-tagline {
    position: absolute;
    left: 0;
    right: 0;
    top: 502px;
    text-align: center;
    font-family: "Roboto", "Helvetica Neue", Arial, sans-serif;
    font-size: 33px;
    font-weight: 300;
    color: var(--panel-text);
    letter-spacing: 1.6px;
  }
  .contact {
    position: absolute;
    left: 622px;
    top: 278px;
  }
  .contact-name {
    font-family: "Arimo", "Helvetica Neue", Arial, sans-serif;
    font-size: 35px;
    font-weight: 700;
    color: var(--name-ink);
    letter-spacing: 2.2px;
    line-height: 44px;
  }
  .contact-line {
    font-family: "Roboto", "Helvetica Neue", Arial, sans-serif;
    font-size: 33px;
    font-weight: 300;
    color: var(--contact-ink);
    letter-spacing: 0.6px;
    line-height: 48px;
  }
</style>
</head>
<body>
  <div class="card">
    <div class="card-edge"></div>
    <div class="brand-panel">
      <svg class="brand-square" viewBox="0 0 190 190" aria-hidden="true">
        <rect x="0" y="0" width="190" height="190" fill="var(--mark-fill)"/>
      </svg>
      <div class="brand-name">BrimstoneHoldingsLLC</div>
      <div class="brand-tagline">Real Estate Investment</div>
    </div>
    <div class="contact">
      <div class="contact-name">Tamsin-Leigh Okafor</div>
      <div class="contact-line">E: BrimstoneHoldings@mailtrove.com</div>
      <div class="contact-line">P: 555-413-2960</div>
    </div>
  </div>
</body>
</html>
```